Music Festival Business Cards

The Lantern Gathering
Produced by Bramblewood Sound Collective LLC
New music festival in Arkansas.

Target Market(s)

18-35 year olds

Industry/Entity Type

Festival

Contact Information for Business Card

We are a 5-partner team producing a music festival in Arkansas. We need slick business cards, and I want them to be square.

Requirements
Must have
• I NEED THESE TO BE IN SQUARE SIZE - 2x2 or 2.5x2.5... please not regular size.
• I need www.lanternmeet.example as the link to website.

```html
<!DOCTYPE html>
<html lang="en">
<head>
<meta charset="utf-8">
<title>The Lantern Gathering — Square Business Cards</title>
<link href="https://fonts.googleapis.com/css2?family=Roboto:wght@300;400;500;700&display=swap" rel="stylesheet">
<style>
  :root {
    --teal: #34cbd3;
    --paper: #f4f4f4;
    --ink: #333a3d;
    --rule: #c9cccd;
    --shade: #b9bcbd;
    --stage: #e6e7e8;
  }
  * { margin: 0; padding: 0; box-sizing: border-box; }
  html, body { width: 1200px; height: 911px; overflow: hidden; }
  body {
    background: var(--stage);
    font-family: "Roboto", Arial, sans-serif;
    position: relative;
  }
  .card {
    position: absolute;
    width: 420px;
    height: 420px;
    overflow: hidden;
    box-shadow: 0 8px 24px rgba(0,0,0,0.18);
  }

  /* Front */
  .card-front { left: 110px; top: 55px; background: var(--paper); }
  .card-front .band { position: absolute; left: 0; bottom: 0; width: 420px; height: 70px; }
  .brand {
    position: absolute; left: 26px; top: 150px; width: 160px;
    display: flex; align-items: center; gap: 10px;
  }
  .brand-mark { width: 14px; height: 14px; background: var(--teal); flex: none; }
  .brand-name {
    color: var(--teal); font-weight: 500; font-size: 18px;
    letter-spacing: 1.5px; text-transform: uppercase; line-height: 1.2;
  }
  .divider {
    position: absolute; left: 196px; top: 62px; width: 1px; height: 230px;
    background: var(--rule);
  }
  .contact { position: absolute; left: 210px; top: 66px; width: 200px; color: var(--ink); }
  .contact .person { color: var(--teal); font-weight: 700; font-size: 17px; text-transform: uppercase; }
  .contact .role { font-weight: 500; font-size: 13px; margin-top: 2px; text-transform: uppercase; }
  .contact .address { font-size: 12px; font-weight: 300; line-height: 1.5; margin-top: 12px; }
  .contact ul { list-style: none; margin-top: 10px; font-size: 12px; font-weight: 300; }
  .contact li { display: flex; align-items: center; gap: 7px; line-height: 1.65; white-space: nowrap; }
  .contact li svg { width: 10px; height: 10px; flex: none; }
  .front-web {
    position: absolute; right: 18px; bottom: 12px;
    color: #fff; font-size: 12px; letter-spacing: 1.5px; white-space: nowrap;
  }

  /* Back */
  .card-back { left: 670px; top: 440px; background: var(--teal); }
  .back-web {
    position: absolute; left: 38px; top: 50%;
    transform: translate(-50%, -50%) rotate(90deg);
    color: #fff; font-size: 11px; letter-spacing: 5px; white-space: nowrap;
  }
  .back-brand {
    position: absolute; left: 90px; top: 50%; width: 290px;
    transform: translateY(-50%);
    display: flex; align-items: center; gap: 14px;
  }
  .back-brand .brand-mark { width: 20px; height: 20px; background: #fff; }
  .back-brand .brand-name { color: #fff; font-size: 26px; }
</style>
</head>
<body>

<section class="card card-front" aria-label="Business card front">
  <svg class="band" viewBox="0 0 420 70" aria-hidden="true">
    <path d="M0 52 H190 Q200 52 204 43 L209 31 Q213 24 223 24 H420 V70 H0 Z" fill="var(--shade)"/>
    <path d="M0 60 H190 Q200 60 204 51 L209 39 Q213 32 223 32 H420 V70 H0 Z" fill="var(--teal)"/>
  </svg>

  <div class="brand">
    <span class="brand-mark"></span>
    <span class="brand-name">The Lantern Gathering</span>
  </div>

  <div class="divider"></div>

  <div class="contact">
    <p class="person">Maren Holt</p>
    <p class="role">CEO/Founder</p>
    <p class="address">214 Cedar Hollow Road<br>Fayetteville, Arkansas 72701</p>
    <ul>
      <li>
        <svg viewBox="0 0 12 12" aria-hidden="true"><path d="M2.5 1 L4.5 1 L5.3 3.6 L4 4.6 Q5 7 7.4 8 L8.4 6.7 L11 7.5 L11 9.5 Q11 11 9.5 11 Q1 10.5 1 2.5 Q1 1 2.5 1 Z" fill="var(--teal)"/></svg>
        555 301 2247
      </li>
      <li>
        <svg viewBox="0 0 12 12" aria-hidden="true"><rect x="3" y="0.5" width="6" height="11" rx="1" fill="none" stroke="var(--teal)" stroke-width="1.2"/><circle cx="6" cy="9.5" r="0.7" fill="var(--teal)"/></svg>
        555 782 4419
      </li>
      <li>
        <svg viewBox="0 0 12 12" aria-hidden="true"><rect x="1" y="4" width="10" height="7" rx="1" fill="var(--teal)"/><rect x="3" y="1" width="6" height="4" fill="none" stroke="var(--teal)" stroke-width="1.2"/></svg>
        555 916 0352
      </li>
      <li>
        <svg viewBox="0 0 12 12" aria-hidden="true"><rect x="0.5" y="0.5" width="11" height="11" rx="1.5" fill="var(--teal)"/><path d="M3 6.2 L5.1 8.2 L9 3.8" fill="none" stroke="#fff" stroke-width="1.4"/></svg>
        maren@lanternmeet.example
      </li>
    </ul>
  </div>

  <p class="front-web">www.lanternmeet.example</p>
</section>

<section class="card card-back" aria-label="Business card back">
  <p class="back-web">www.lanternmeet.example</p>
  <div class="back-brand">
    <span class="brand-mark"></span>
    <span class="brand-name">The Lantern Gathering</span>
  </div>
</section>

</body>
</html>
```